Motor Vault Website - Part of the Brantley Group

A complimentary website is required for the launch of a 'Motor Vault' - a new service launched by industry renowned BRANTLEY. Motor Vault is an industry-first brand that designs and builds unique subterranean car parks for private residential homes in London and the influential counties within the UK. Please see here the direction of a new BRANTLEY Website - we would like Motor Vault to be complimentary and sit alongside BRANTLEY harmoniously - https://www.brantleyhq.example/brantley-nu-staging Brantley have some images, but whilst more professional images are in production - we have also attached pixmoor photos- named clearly as pixmoor. **Attached files include JPEG, .eps of logo and Brantley library images and Pixmoor Library Images - two versions of logo dependent on background colour. - Website needs to be sleek, chic and masculine.- Colour Palette - Grey/ Black/ White - Same visiual journey as Brantley website- Required areas within the sit include - About Us / Our Work / Contact Page

Target Market(s)

Luxury
Men

Number of Pages Required

2 page

Font styles to use
Sans Serif

Colors
e8e8e8
757575
1b1b1b
000000
9d9d9d
cbcbcb
f5f5f5

Requirements
Must have
• Complimentary of this site - https://www.brantleyhq.example/brantley-nu-staging
Should not have
• Colour

```html
<!DOCTYPE html>
<html lang="en">
<head>
<meta charset="utf-8">
<title>Motor Vault – Part of the Brantley Group</title>
<link href="https://fonts.googleapis.com/css2?family=Fira+Sans:wght@400;500;600;700&display=swap" rel="stylesheet">
<style>
  :root {
    --black: #000000;
    --ink: #1b1b1b;
    --navy-ink: #10122a;
    --grey-dark: #757575;
    --grey-mid: #9d9d9d;
    --grey-light: #cbcbcb;
    --off-white: #e8e8e8;
    --white: #ffffff;
    --panel-border: #5a5a5a;
  }
  * { box-sizing: border-box; margin: 0; padding: 0; }
  html, body { width: 1200px; height: 1000px; overflow: hidden; }
  body {
    position: relative;
    background: #fbfbfb;
    font-family: "Fira Sans", sans-serif;
    color: var(--white);
  }

  /* Hero */
  .hero {
    position: absolute; left: 0; top: 0; width: 1200px; height: 582px;
    overflow: hidden;
  }
  .hero-photo {
    position: absolute; inset: 0;
    background:
      radial-gradient(ellipse 260px 150px at 600px 420px, #8a8a8a 0%, #4a4a4a 45%, transparent 100%),
      linear-gradient(180deg, #0b0b0b 0%, #1d1d1d 25%, #2c2c2c 60%, #1a1a1a 100%);
  }
  .brand {
    position: absolute; left: 56px; top: 30px;
    display: flex; flex-direction: column;
  }
  .brand-name {
    font-size: 27px; font-weight: 500; letter-spacing: 0.5px;
    line-height: 1; text-transform: uppercase; color: var(--white);
  }
  .brand-tag {
    margin-top: 3px; font-size: 6px; letter-spacing: 0.6px;
    color: var(--grey-mid); text-transform: uppercase;
  }
  .menu {
    position: absolute; left: 1047px; top: 28px;
    display: flex; align-items: center;
  }
  .menu-label { font-size: 17px; margin-right: 10px; }
  .menu-button {
    width: 47px; height: 44px; border: 2px solid var(--white);
    display: flex; align-items: center; justify-content: center;
  }
  .headline {
    position: absolute; left: 53px; top: 176px;
    font-size: 48px; font-weight: 600; line-height: 54px;
    color: var(--off-white);
  }
  .subline {
    position: absolute; left: 107px; top: 306px;
    font-size: 24px; line-height: 36px; color: var(--off-white);
  }
  .subline-rule {
    position: absolute; left: 57px; top: 322px;
    width: 34px; height: 2px; background: var(--grey-mid);
  }
  .side-nav {
    position: absolute; left: 973px; top: 225px; width: 227px; height: 176px;
    background: rgba(0,0,0,0.45);
  }
  .side-nav-item {
    height: 59px; padding: 12px 0 0 34px; position: relative;
    border-bottom: 1px solid rgba(255,255,255,0.2);
  }
  .side-nav-item:last-child { border-bottom: none; }
  .side-nav-item::before {
    content: ""; position: absolute; left: 19px; top: 17px;
    width: 6px; height: 6px; border-radius: 50%; background: var(--grey-mid);
  }
  .side-nav-title { font-size: 13px; text-transform: uppercase; color: var(--off-white); display: block; }
  .side-nav-sub { font-size: 11px; color: var(--grey-dark); display: block; margin-top: 2px; }
  .scroll-cue {
    position: absolute; left: 570px; top: 492px; width: 70px;
    text-align: center; font-size: 12px; color: var(--grey-dark);
  }
  .scroll-cue svg { display: block; margin: 0 auto 6px; }
  .follow {
    position: absolute; left: 57px; top: 540px;
    display: flex; align-items: center; font-size: 10px; color: var(--white);
  }
  .follow-rule { width: 30px; height: 1px; background: var(--grey-dark); margin: 0 8px; }
  .follow a { color: var(--white); text-decoration: none; margin-right: 13px; }

  /* Services */
  .services { position: absolute; left: 0; top: 582px; width: 1200px; height: 383px; }
  .tile { position: absolute; top: 0; height: 383px; }
  .tile-photo-corridor {
    left: 0; width: 284px;
    background: linear-gradient(100deg, #1a1a1a 0%, #555 40%, #9a9a9a 55%, #2a2a2a 80%, #111 100%);
  }
  .tile-photo-steel {
    left: 613px; width: 273px;
    background: linear-gradient(135deg, #cfcfcf 0%, #5e5e5e 35%, #e0e0e0 60%, #3a3a3a 85%, #a9a9a9 100%);
  }
  .tile-residential { left: 284px; width: 329px; background: var(--white); padding: 44px 30px 0 30px; }
  .tile-construction { left: 886px; width: 314px; background: var(--ink); }
  .tile-frame {
    position: absolute; left: 18px; top: 18px; width: 284px; height: 346px;
    border: 2px solid var(--panel-border); padding: 26px 0 0 14px;
  }
  .tile-heading {
    font-size: 35px; font-weight: 600; line-height: 37px; text-transform: uppercase;
  }
  .tile-text {
    margin-top: 16px; font-size: 16px; font-weight: 600; line-height: 27px;
    text-transform: uppercase; letter-spacing: 0.3px;
  }
  .tile-residential .tile-heading, .tile-residential .tile-text { color: var(--navy-ink); }
  .tile-construction .tile-heading { color: var(--white); }
  .tile-construction .tile-text { color: var(--white); line-height: 23px; margin-left: 6px; margin-top: 18px; }
</style>
</head>
<body>

<header class="hero">
  <div class="hero-photo" role="img" aria-label="Black and white photo of an empty concrete underground car park with steel columns"></div>

  <div class="brand">
    <span class="brand-name">Motor Vault</span>
    <span class="brand-tag">Part of the Brantley Group</span>
  </div>

  <div class="menu">
    <span class="menu-label">Menu</span>
    <span class="menu-button">
      <svg width="12" height="10" viewBox="0 0 12 10"><rect y="0" width="12" height="2" fill="#fff"/><rect y="4" width="12" height="2" fill="#fff"/><rect y="8" width="12" height="2" fill="#fff"/></svg>
    </span>
  </div>

  <h1 class="headline">A carving cave where your<br>vehical can take rest</h1>
  <span class="subline-rule"></span>
  <p class="subline">Specialising turnkey solutions for Basements,<br>Shell &amp; Core and Interior Fit-Out</p>

  <nav class="side-nav">
    <div class="side-nav-item"><span class="side-nav-title">About</span><span class="side-nav-sub">Who we are</span></div>
    <div class="side-nav-item"><span class="side-nav-title">Blog</span><span class="side-nav-sub">Whats New</span></div>
    <div class="side-nav-item"><span class="side-nav-title">Contact</span><span class="side-nav-sub">get in touch</span></div>
  </nav>

  <div class="scroll-cue">
    <svg width="20" height="30" viewBox="0 0 20 30"><rect x="1" y="1" width="18" height="28" rx="9" fill="none" stroke="#757575" stroke-width="1.5"/><line x1="10" y1="7" x2="10" y2="12" stroke="#757575" stroke-width="1.5"/></svg>
    Scroll Down
  </div>

  <div class="follow">
    <span>Follow Us</span>
    <span class="follow-rule"></span>
    <a href="#">Circlebook</a>
    <a href="#">Chirper</a>
    <a href="#">Linkwork</a>
  </div>
</header>

<section class="services">
  <div class="tile tile-photo-corridor" role="img" aria-label="Black and white photo of a concrete corridor with sunlight falling through columns"></div>

  <article class="tile tile-residential">
    <h2 class="tile-heading">Residential<br>Basements</h2>
    <p class="tile-text">Under existing London properties, Brantley can create single or double depth basements to provide extra living space for a multitude of uses. We can also provide</p>
  </article>

  <div class="tile tile-photo-steel" role="img" aria-label="Black and white photo looking up at a steel beam construction frame"></div>

  <article class="tile tile-construction">
    <div class="tile-frame">
      <h2 class="tile-heading">Construction<br>&amp; Design</h2>
      <p class="tile-text">We provide complete project management services to support buildings and basement constructions projects. Works include:</p>
    </div>
  </article>
</section>

</body>
</html>
```